Industrial Company-Pop-Up Banner Design for Demolition and Infrastructure Company

Hi-
We need to create 2 pop-up banners for our company. They will both have the same logo, but different photos. We would like to have the colors white, red, and black and feature a modern design. I have attached some inspiration photos.

Target Market(s)

Trade Show/Job Fair Audience

Industry/Entity Type

construction, industrial

Font styles to use
Sans Serif

Colors
EB3D1F
EC4F4E
F09395
F8D3D4
FCEDEE

Requirements
Must have
• 2 versions, each with different photos but same design. Logo, Red, Black, and White Color Scheme, Modern Design
Nice to have
• Modern Design similar to the inspiration photos

```html
<!DOCTYPE html>
<html lang="en">
<head>
<meta charset="utf-8">
<title>Halvorsen Group Pop-Up Banners</title>
<link rel="stylesheet" href="https://fonts.googleapis.com/css2?family=Anton&family=Yellowtail&family=Dancing+Script:wght@700&display=swap">
<style>
  :root {
    --stage: #8e8e8e;
    --stage-light: #a3a3a3;
    --banner: #f4f4f4;
    --red: #d7262b;
    --black: #1a1a1a;
    --frame: #7a7a7a;
  }
  * { box-sizing: border-box; margin: 0; padding: 0; }
  html, body { width: 1200px; height: 1086px; overflow: hidden; }
  body {
    background: radial-gradient(ellipse at 50% 40%, var(--stage-light), var(--stage) 75%);
    position: relative;
    font-family: "Anton", sans-serif;
  }
  .banner {
    position: absolute;
    top: 208px;
    width: 232px;
    height: 650px;
    background: var(--banner);
    box-shadow: 0 6px 18px rgba(0,0,0,0.18);
  }
  .banner--left { left: 244px; }
  .banner--right { left: 720px; }
  .brand {
    height: 125px;
    display: flex;
    align-items: center;
    justify-content: center;
    gap: 8px;
  }
  .brand__mark { width: 16px; height: 16px; background: var(--red); }
  .brand__name {
    color: var(--red);
    font-family: "Anton", sans-serif;
    font-size: 22px;
    letter-spacing: 0.5px;
  }
  .hero {
    height: 322px;
    border-top: 4px solid var(--red);
    border-bottom: 4px solid var(--red);
  }
  .hero--plant {
    background: linear-gradient(180deg, #d8dde2 0%, #a9b6c2 45%, #7f96a8 62%, #6f7f78 80%, #4d6b3f 100%);
  }
  .hero--facility {
    background: linear-gradient(180deg, #5b95cf 0%, #a9c9e6 25%, #4f7fb0 45%, #6e6a62 70%, #e4e4e0 86%, #5f8f3a 100%);
  }
  .thumbs {
    display: flex;
    justify-content: space-between;
    padding: 14px 11px 0;
  }
  .thumb {
    width: 64px;
    height: 55px;
    border: 2px solid #fff;
    outline: 1px solid var(--frame);
  }
  .thumb--site { background: linear-gradient(180deg, #6fa0d4 0%, #8aa86a 35%, #d9b38c 60%, #c98d63 100%); }
  .thumb--hangar { background: linear-gradient(180deg, #4c7fb8 0%, #c9c9c9 45%, #e0c640 70%, #8a8a8a 100%); }
  .thumb--ruins { background: linear-gradient(180deg, #5c8fc8 0%, #9aa0a8 45%, #d8d8d2 72%, #6c9443 100%); }
  .thumb--marsh { background: linear-gradient(180deg, #8fb6d8 0%, #5f8fb4 40%, #5c8a4a 75%, #3f6a30 100%); }
  .tagline {
    text-align: center;
    padding-top: 16px;
    position: relative;
  }
  .tagline__lead {
    color: var(--black);
    font-size: 27px;
    line-height: 1;
  }
  .tagline__script {
    position: relative;
    height: 38px;
    margin-top: 2px;
  }
  .tagline__rule {
    position: absolute;
    left: 0; right: 0; top: 22px;
    height: 1px;
    background: var(--red);
  }
  .tagline__word {
    position: relative;
    display: inline-block;
    padding: 0 6px;
    background: var(--banner);
    color: var(--red);
    font-family: "Yellowtail", "Dancing Script", cursive;
    font-size: 30px;
    line-height: 38px;
  }
  .tagline__since {
    color: var(--black);
    font-size: 13px;
    margin-top: 6px;
  }
</style>
</head>
<body>
  <section class="banner banner--left">
    <header class="brand">
      <span class="brand__mark"></span>
      <span class="brand__name">HALVORSEN GROUP</span>
    </header>
    <div class="hero hero--plant" role="img" aria-label="Power plant with red and white smokestacks during a controlled demolition"></div>
    <div class="thumbs">
      <div class="thumb thumb--site" role="img" aria-label="Excavators grading a dirt site"></div>
      <div class="thumb thumb--hangar" role="img" aria-label="Excavator beside a tall industrial hangar"></div>
      <div class="thumb thumb--ruins" role="img" aria-label="Partially demolished industrial facility"></div>
    </div>
    <div class="tagline">
      <p class="tagline__lead">Building Better</p>
      <div class="tagline__script"><span class="tagline__rule"></span><span class="tagline__word">Cities</span></div>
      <p class="tagline__since">Since 1972.</p>
    </div>
  </section>

  <section class="banner banner--right">
    <header class="brand">
      <span class="brand__mark"></span>
      <span class="brand__name">HALVORSEN GROUP</span>
    </header>
    <div class="hero hero--facility" role="img" aria-label="Blue industrial building mid-demolition with excavators and rubble"></div>
    <div class="thumbs">
      <div class="thumb thumb--site" role="img" aria-label="Excavator working on a red clay site"></div>
      <div class="thumb thumb--marsh" role="img" aria-label="Aerial view of a waterfront industrial site"></div>
      <div class="thumb thumb--site" role="img" aria-label="Earthmoving equipment on a cleared lot"></div>
    </div>
    <div class="tagline">
      <p class="tagline__lead">Building Better</p>
      <div class="tagline__script"><span class="tagline__rule"></span><span class="tagline__word">Cities</span></div>
      <p class="tagline__since">Since 1972.</p>
    </div>
  </section>
</body>
</html>
```